Real Estate Entrepreneur needs a business card

I am a real estate entrepreneur, I buy houses for investment purposes, I act as a real estate agent representing buyers and sellers in residential home transactions, I am a contractor that does a wide range of home repairs and construction. I'd like a design that can stick with me through the years as my business grows and morphs to fit any niche I decide to pursue as markets change.

Target Market(s)

Anyone with interest that may be related to real estate.

Industry/Entity Type

Real Estate

Contact Information for Business Card

A card that stands out and doesn't put me in any one box. My business will evolve over time and I need a card that can stay relevant.

Colors

Designer to choose colors to be used in the design.

Requirements
Must have
• Character
Nice to have
• I'm open
Should not have
• Cliche houses and hammers

```html
<!DOCTYPE html>
<html lang="en">
<head>
<meta charset="utf-8">
<title>Holt Rivers — Business Card</title>
<link href="https://fonts.googleapis.com/css2?family=Crimson+Text:wght@400;600&display=swap" rel="stylesheet">
<style>
  :root {
    --backdrop: #3a3a3a;
    --card: #f3f3f1;
    --ink: #1c1c1c;
    --artwork-tone: #e4e4e1;
  }
  * { margin: 0; padding: 0; box-sizing: border-box; }
  html, body {
    width: 1200px;
    height: 755px;
    overflow: hidden;
    background: var(--backdrop);
  }
  .canvas {
    position: relative;
    width: 1200px;
    height: 755px;
  }
  .card {
    position: absolute;
    top: 218px;
    width: 496px;
    height: 287px;
    background: var(--card);
  }
  .card--front { left: 90px; }
  .card--back { left: 622px; }

  .brand {
    position: absolute;
    right: 24px;
    bottom: 44px;
    text-align: left;
    color: var(--ink);
    font-family: "Crimson Text", Georgia, serif;
  }
  .brand__name {
    font-size: 27px;
    font-weight: 400;
    letter-spacing: 1.6px;
    line-height: 1;
  }
  .brand__tagline {
    margin-top: 5px;
    font-size: 9px;
    font-weight: 600;
    letter-spacing: 2.3px;
    line-height: 1;
  }

  .skyline {
    position: absolute;
    left: 0;
    top: 0;
  }
</style>
</head>
<body>
  <main class="canvas">
    <section class="card card--front">
      <div class="brand">
        <div class="brand__name">HOLT RIVERS</div>
        <div class="brand__tagline">PREMIUM REAL ESTATE</div>
      </div>
    </section>

    <section class="card card--back">
      <svg class="skyline" width="496" height="287" viewBox="0 0 496 287">
        <rect x="11" y="193" width="88" height="81" fill="var(--artwork-tone)" role="img" aria-label="Single-line drawing of a city skyline"/>
        <line x1="99" y1="274" x2="496" y2="274" stroke="var(--ink)" stroke-width="1.4"/>
      </svg>
    </section>
  </main>
</body>
</html>
```